fernbolt website

commerce website to sell cookeries, brackets, mailboxes and to show off homes built. Modern Steel in design see kelvo rides web page to be like: https://www.kelvorides.com/en/ sorry its blue mantis hosting word press divi

must be able to add products to page

Target Market(s)

mainly western states of U.S.

Industry/Entity Type

Building Product

Coding

Coded - Design and coding required

Number of Pages Required

3 page

Font styles to use
Sans Serif

Colors

Designer to choose colors to be used in the design.

Requirements
Must have
• customers to be able to order products from page
• blue mantis hosting word press divi

```html
<!DOCTYPE html>
<html lang="en">
<head>
<meta charset="utf-8">
<title>Fernbolt – Pressure Cooker with Inner Lid</title>
<link rel="stylesheet" href="https://fonts.googleapis.com/css2?family=Open+Sans:wght@400;600;700&family=Roboto:wght@700;900&display=swap">
<style>
:root{
  --header:#425c88;
  --page:#ebecee;
  --white:#ffffff;
  --ink:#222222;
  --muted:#6b6b6b;
  --accent:#fba55c;
  --link:#3a6fc4;
  --price:#2f4a8a;
  --stock:#3a8a1e;
  --promo-dark:#363538;
  --promo-gold:#ffd21c;
  --sale:#ffd400;
  --band:#4b5d79;
  --footer:#253149;
  --footer-base:#1d2536;
  --star:#f5b800;
}
*{box-sizing:border-box;margin:0;padding:0}
html,body{width:1200px;height:2228px;overflow:hidden}
body{position:relative;background:var(--page);font-family:"Open Sans",sans-serif;color:var(--ink)}
.abs{position:absolute}

.site-header{left:0;top:0;width:1200px;height:75px;background:var(--header)}
.brand{left:36px;top:14px;width:112px;text-align:center;color:var(--white);font-size:17px;font-weight:600;letter-spacing:.5px}
.brand-mark{display:block;margin:0 auto 6px;width:18px;height:18px;border-radius:50%;background:var(--white)}
.search{left:162px;top:9px;width:704px;height:24px;background:var(--white);border-radius:2px}
.search-scope{left:0;top:0;width:46px;height:24px;background:#e8e8e8;font-size:11px;color:#555;padding:4px 6px}
.search-btn{right:0;top:0;width:32px;height:24px;background:var(--accent);display:flex;align-items:center;justify-content:center}
.main-nav{left:190px;top:48px;display:flex;gap:36px;color:var(--white);font-size:12px}
.utility{right:40px;top:13px;display:flex;gap:14px;align-items:center;color:var(--white);font-size:12px}
.utility span{display:flex;align-items:center;gap:6px}
.cart-count{position:absolute;right:-8px;top:-6px;width:15px;height:15px;border-radius:50%;background:var(--accent);font-size:9px;text-align:center;line-height:15px}

.breadcrumb{left:79px;top:105px;font-size:12px;display:flex;gap:10px;color:#333}

.product-photo{left:60px;top:255px;width:332px;height:210px;border-radius:50% 50% 30% 30%/40% 40% 25% 25%;background:radial-gradient(ellipse at 40% 40%,#f4f4f4,#c9c9c9 60%,#9a9a9a)}
.zoom{left:348px;top:197px;width:21px;height:21px;background:var(--white);border:1px solid #ddd;display:flex;align-items:center;justify-content:center}
.thumb{top:518px;width:61px;height:60px;border:1px solid #ccc;background:linear-gradient(#ffffff,#d9d9d9)}

.product-info{left:416px;top:186px;width:460px}
.product-title{font-size:18px;font-weight:600;line-height:20px;letter-spacing:.3px}
.meta{margin-top:15px;font-size:12px;line-height:21px}
.meta div{display:flex}
.meta b{font-weight:400;width:82px}
.meta span{color:var(--muted)}
.price{margin-top:14px;font-size:17px;font-weight:600}
.price s{color:#999;margin-right:8px}
.price span{color:var(--price)}
.summary{margin-top:12px;font-size:13px;line-height:18px;color:var(--muted)}
.stock{margin-top:14px;font-size:12px;font-weight:700;color:var(--stock)}
.buy{margin-top:12px;display:flex;gap:7px;align-items:center}
.qty-btn{width:30px;height:29px;border:1px solid #ccc;background:#f6f6f6;color:#888;display:flex;align-items:center;justify-content:center;font-size:16px}
.qty{width:44px;height:29px;border:1px solid #ccc;background:var(--white);text-align:center;line-height:27px;font-size:13px}
.add-cart{margin-left:2px;width:105px;height:29px;background:var(--accent);color:var(--white);font-size:11px;font-weight:700;letter-spacing:.5px;text-align:center;line-height:29px}
.extras{margin-top:19px;display:flex;gap:17px;font-size:12px;color:#333}

.promo{left:922px;top:189px;width:203px;height:304px;background:var(--promo-dark);text-align:center}
.promo h3{margin-top:21px;color:var(--promo-gold);font-size:15px;font-weight:600}
.promo p{color:#ddd;font-size:12px;margin-top:3px}
.promo-art{left:30px;top:80px;width:144px;height:175px;border-radius:40%;background:radial-gradient(circle at 50% 50%,#b0243a,#5a1a25 60%,var(--promo-dark) 75%)}
.dot{top:499px;width:7px;height:7px;border-radius:50%}
.sale{left:923px;top:518px;width:202px;height:127px;background:var(--sale);text-align:center;font-family:"Roboto",sans-serif;color:#000}
.sale .big{font-size:32px;font-weight:900;margin-top:15px;line-height:34px}
.sale .small{margin:4px auto 0;width:138px;border-top:1px dashed #333;border-bottom:1px dashed #333;font-size:10px;font-weight:700;padding:4px 0}
.sale .off{font-size:32px;font-weight:900;line-height:40px}

.tabs{left:74px;top:737px;height:47px;display:flex;font-size:13px}
.tab{padding:0 24px;line-height:47px;color:#666}
.tab.active{background:var(--white);color:var(--ink);font-weight:600}
.panel{left:75px;top:784px;width:1048px;height:583px;background:var(--white)}
.panel h2{position:absolute;left:37px;top:70px;font-size:17px;font-weight:600}
.qa-search{position:absolute;left:38px;top:114px;width:972px;height:41px;border:1px solid #bbb;display:flex;align-items:center;gap:12px;padding-left:14px;font-size:12px;color:#888}
.qa{position:absolute;left:43px;width:820px;font-size:12px}
.qa .row{display:flex}
.qa .lbl{width:106px;flex:none}
.qa .q{color:var(--link)}
.qa .a{color:var(--muted);line-height:18px}
.qa .row+.row{margin-top:13px}
.more{position:absolute;left:150px;top:498px;width:212px;height:34px;background:var(--accent);color:var(--white);font-size:12px;text-align:center;line-height:34px}

.related-title{left:76px;top:1408px;font-size:18px;font-weight:600;letter-spacing:.3px}
.card{top:1441px;width:262px;height:316px;background:var(--white)}
.card h4{margin:22px 0 0 24px;font-size:16px;font-weight:700;letter-spacing:.4px;white-space:nowrap}
.card .pic{position:absolute;left:14px;top:48px;width:233px;height:188px}
.card p{position:absolute;left:15px;top:253px;width:236px;font-size:12.5px;line-height:15px;color:var(--muted)}
.stars{position:absolute;left:17px;top:293px;display:flex;gap:4px}

.to-top{left:0;top:1801px;width:1200px;height:37px;background:var(--band);color:var(--white);text-align:center;line-height:37px;font-size:14px}
.footer{left:0;top:1838px;width:1200px;height:342px;background:var(--footer);color:var(--white)}
.fcol{position:absolute;top:112px;font-size:12px;line-height:19.5px}
.fcol h5{font-size:14px;font-weight:700;margin-bottom:3px;letter-spacing:.3px}
.base{left:0;top:2180px;width:1200px;height:48px;background:var(--footer-base);color:var(--white);text-align:center;line-height:48px;font-size:12px}
</style>
</head>
<body>

<header class="site-header abs">
  <div class="brand abs"><span class="brand-mark"></span>Fernbolt</div>
  <div class="search abs">
    <div class="search-scope abs">ALL ▾</div>
    <div class="search-btn abs"><svg width="12" height="12" viewBox="0 0 12 12"><circle cx="5" cy="5" r="3.6" fill="none" stroke="#fff" stroke-width="1.6"/><path d="M7.6 7.6L11 11" stroke="#fff" stroke-width="1.8"/></svg></div>
  </div>
  <nav class="main-nav abs"><span>Home</span><span>Product</span><span>Who We Are</span><span>Contact</span></nav>
  <div class="utility abs">
    <span><svg width="11" height="12" viewBox="0 0 11 12"><circle cx="5.5" cy="3.2" r="2.8" fill="#fff"/><path d="M0 12c0-4 2.5-5.5 5.5-5.5S11 8 11 12z" fill="#fff"/></svg>Login / Sign Up</span>
    <span><svg width="13" height="12" viewBox="0 0 13 12"><rect x="1" y="3" width="8" height="8" fill="none" stroke="#fff" stroke-width="1.4"/><path d="M6 6l6-5M9 1h3v3" stroke="#fff" stroke-width="1.4" fill="none"/></svg>Returns</span>
    <span style="position:relative;margin-left:16px"><svg width="16" height="14" viewBox="0 0 16 14"><path d="M0 1h3l2 8h9l2-6H4" fill="#fff"/><circle cx="6" cy="12" r="1.5" fill="#fff"/><circle cx="13" cy="12" r="1.5" fill="#fff"/></svg><em class="cart-count" style="font-style:normal">0</em></span>
  </div>
</header>

<div class="breadcrumb abs"><span>Home</span><span>»</span><span>Products</span><span>»</span><span>Pressure Cooker with Inner Lid, 5 litres, Silver</span></div>

<div class="product-photo abs" role="img" aria-label="Silver pressure cooker with black handles"></div>
<div class="zoom abs"><svg width="11" height="11" viewBox="0 0 12 12"><circle cx="5" cy="5" r="3.6" fill="none" stroke="#222" stroke-width="1.6"/><path d="M7.6 7.6L11 11" stroke="#222" stroke-width="1.8"/></svg></div>
<div class="thumb abs" style="left:77px" role="img" aria-label="Pressure cooker thumbnail"></div>
<div class="thumb abs" style="left:158px" role="img" aria-label="Pressure cooker with box thumbnail"></div>
<div class="thumb abs" style="left:238px" role="img" aria-label="Pressure cooker in kitchen thumbnail"></div>

<section class="product-info abs">
  <h1 class="product-title">Pressure Cooker with Inner Lid,<br>5 litres, Silver</h1>
  <div class="meta">
    <div><b>SKU:</b><span>NLM45</span></div>
    <div><b>Categories:</b><span>Cooker</span></div>
    <div><b>Tags:</b><span>Cooking Items, Cookeries</span></div>
  </div>
  <div class="price"><s>$55.00</s><span>$48.00</span></div>
  <p class="summary">Quis autem vel eum iure reprehenderit qui in ea voluptate velit esse quam nihil molestiae consequatur, vel illum qui dolorem eum fugiat quo voluptas nulla pariatur quis nostrum exercitationem ullam corporis</p>
  <div class="stock">In stock</div>
  <div class="buy">
    <div class="qty-btn">−</div><div class="qty">1</div><div class="qty-btn">+</div>
    <div class="add-cart">ADD TO CART</div>
  </div>
  <div class="extras"><span>♥ Add To Wishlist</span><span>▥ Compare</span></div>
</section>

<aside class="promo abs">
  <h3>Upto 60 % Flate</h3>
  <p>Festival Season is Here</p>
  <div class="promo-art abs" role="img" aria-label="Red cookware set with pans and utensils"></div>
</aside>
<div class="dot abs" style="left:1013px;background:#ccc"></div>
<div class="dot abs" style="left:1025px;background:#111"></div>
<div class="sale abs">
  <div class="big">SALE</div>
  <div class="small">SAVE UP TO</div>
  <div class="off">35% OFF</div>
</div>

<div class="tabs abs"><div class="tab active">Questions &amp; Answers</div><div class="tab">Description</div><div class="tab" style="padding-left:4px">Reviews</div></div>
<section class="panel abs">
  <h2>Customer questions &amp; answers</h2>
  <div class="qa-search"><svg width="11" height="11" viewBox="0 0 12 12"><circle cx="5" cy="5" r="3.6" fill="none" stroke="#888" stroke-width="1.6"/><path d="M7.6 7.6L11 11" stroke="#888" stroke-width="1.8"/></svg>Have a questions ? Search for answers</div>
  <div class="qa" style="top:177px"><div class="row"><span class="lbl">Question:</span><span class="q">Nemo enim ipsam voluptatem quia voluptas sit aspernatur ?</span></div><div class="row"><span class="lbl">Answer:</span><span class="a">Neque porro quisquam est, qui dolorem ipsum quia dolor sit amet, consectetur, adipisci velit, sed quia non numquam eius modi tempora incidunt ut labore et dolore magnam aliquam quaerat voluptatem. Ut enim ad minima veniam, quis nostrum exercitationem ullam corporis suscipit laboriosam, nisi ut aliquid ex ea commodi consequatur</span></div></div>
  <div class="qa" style="top:284px"><div class="row"><span class="lbl">Question:</span><span class="q">Nemo enim ipsam voluptatem quia voluptas sit aspernatur ?</span></div><div class="row"><span class="lbl">Answer:</span><span class="a">Neque porro quisquam est, qui dolorem ipsum quia dolor sit amet, consectetur, adipisci velit, sed quia non numquam eius modi tempora incidunt ut labore et dolore magnam aliquam quaerat voluptatem. Ut enim ad minima veniam, quis nostrum exercitationem ullam corporis suscipit laboriosam, nisi ut aliquid ex ea commodi consequatur</span></div></div>
  <div class="qa" style="top:391px"><div class="row"><span class="lbl">Question:</span><span class="q">Nemo enim ipsam voluptatem quia voluptas sit aspernatur ?</span></div><div class="row"><span class="lbl">Answer:</span><span class="a">Neque porro quisquam est, qui dolorem ipsum quia dolor sit amet, consectetur, adipisci velit, sed quia non numquam eius modi tempora incidunt ut labore et dolore magnam aliquam quaerat voluptatem. Ut enim ad minima veniam, quis nostrum exercitationem ullam corporis suscipit laboriosam, nisi ut aliquid ex ea commodi consequatur</span></div></div>
  <div class="more">See more answered questions ( 30 )</div>
</section>

<h3 class="related-title abs">Related Products</h3>
<article class="card abs" style="left:53px"><h4>Base Aluminium Cooker ...</h4><div class="pic" role="img" aria-label="Aluminium pressure cookers" style="background:radial-gradient(ellipse at 50% 50%,#cfcfcf,#ececec 60%)"></div><p>Quis autem vel eum iure reprehenderit qui in ea voluptate velit molestiae</p><div class="stars"><svg width="80" height="11" viewBox="0 0 80 11"><g fill="#f5b800"><path id="s1" d="M5.5 0l1.6 3.6 3.9.4-2.9 2.6.8 3.9-3.4-2-3.4 2 .8-3.9L0 4l3.9-.4z"/><use href="#s1" x="15"/><use href="#s1" x="30"/><use href="#s1" x="45"/><use href="#s1" x="60"/></g></svg></div></article>
<article class="card abs" style="left:330px"><h4>Stainless Steel Cookware ...</h4><div class="pic" role="img" aria-label="Stainless steel pots and pans" style="background:radial-gradient(ellipse at 50% 50%,#bdbdbd,#ececec 65%)"></div><p>Quis autem vel eum iure reprehenderit qui in ea voluptate velit molestiae</p><div class="stars"><svg width="80" height="11" viewBox="0 0 80 11"><g fill="#f5b800"><path id="s2" d="M5.5 0l1.6 3.6 3.9.4-2.9 2.6.8 3.9-3.4-2-3.4 2 .8-3.9L0 4l3.9-.4z"/><use href="#s2" x="15"/><use href="#s2" x="30"/><use href="#s2" x="45"/><use href="#s2" x="60"/></g></svg></div></article>
<article class="card abs" style="left:608px"><h4>Stainless Steel Rice Cooker ...</h4><div class="pic" role="img" aria-label="Stainless steel rice cooker" style="background:radial-gradient(ellipse at 50% 50%,#b5b5b5,#ececec 55%)"></div><p>Quis autem vel eum iure reprehenderit qui in ea voluptate velit molestiae</p><div class="stars"><svg width="80" height="11" viewBox="0 0 80 11"><g fill="#f5b800"><path id="s3" d="M5.5 0l1.6 3.6 3.9.4-2.9 2.6.8 3.9-3.4-2-3.4 2 .8-3.9L0 4l3.9-.4z"/><use href="#s3" x="15"/><use href="#s3" x="30"/><use href="#s3" x="45"/><use href="#s3" x="60"/></g></svg></div></article>
<article class="card abs" style="left:885px"><h4>Stainless Steel 6-Plates Idly ...</h4><div class="pic" role="img" aria-label="Stainless steel idly cooker with plates" style="background:radial-gradient(ellipse at 45% 55%,#c2c2c2,#ececec 60%)"></div><p>Quis autem vel eum iure reprehenderit qui in ea voluptate velit molestiae</p><div class="stars"><svg width="80" height="11" viewBox="0 0 80 11"><g fill="#f5b800"><path id="s4" d="M5.5 0l1.6 3.6 3.9.4-2.9 2.6.8 3.9-3.4-2-3.4 2 .8-3.9L0 4l3.9-.4z"/><use href="#s4" x="15"/><use href="#s4" x="30"/><use href="#s4" x="45"/><use href="#s4" x="60"/></g></svg></div></article>

<div class="to-top abs">Back To Top</div>
<footer class="footer abs">
  <div class="fcol" style="left:236px"><h5>Get to Know Us</h5>About Us<br>Careers<br>Press Releases<br>Fernbolt Cares<br>Gift a Smile</div>
  <div class="fcol" style="left:409px"><h5>Get to Know Us</h5>Friendspace<br>Chirper<br>Snapgram</div>
  <div class="fcol" style="left:590px"><h5>Make Money with Us</h5>Sell on Fernbolt<br>Sell under Fernbolt<br>Accelerator<br>Become an Affiliate<br>Fulfilment by Fernbolt<br>Advertise Your Products<br>Fernbolt Pay on<br>Merchants</div>
  <div class="fcol" style="left:811px"><h5>Let Us Help You</h5>Your Account<br>Returns Centre<br>100% Purchase<br>Protection<br>Download<br>Help</div>
</footer>
<div class="base abs">©Copyright information here</div>

</body>
</html>
```